Social media app sign-up flow that asks users to give personal info and connect with other apps

Design an interactive, fun, and playful sign-up flow in which you are providing information about you, your interests, and connecting with different API plug-ins such as Fendora, WorkLoop, Tunevo, etc. (using the brand palette attached).

Basic wireframe, and business requirements are also attached.

Target Market(s)

Gen Z + Millennials (ages 22-40)

Font styles to use
Sans Serif

Colors
fbed22
fbee3d
fbf289

Requirements
Must have
• Forms for users to submit their info. Follow the color palette attached.

Connect with Fendora, Connect with WorkLoop, Connect with Tunevo, Connect with Gatherwick buttons
Nice to have
• I like the way you can use cards to submit your information for each category. Interactive card design for providing your info
Should not have
• Basic outdated designs, long forms

```html
<!DOCTYPE html>
<html lang="en">
<head>
<meta charset="utf-8">
<title>Tell me about you: sign-up flow, gold variations</title>
<link href="https://fonts.googleapis.com/css2?family=Comfortaa:wght@400;600&family=Fira+Mono&display=swap" rel="stylesheet">
<style>
  :root {
    --page: #ffffff;
    --stage: #f1f0ea;
    --sheet: #f3f4f6;
    --card: #ffffff;
    --gold: #cbb271;
    --gold-deep: #97844f;
    --gold-pale: #f4efe2;
    --cream: #fbf0d0;
    --sun: #fdc22e;
    --sun-pale: #fdf1c8;
    --slate: #5c6677;
    --slate-deep: #434b59;
    --mist: #b4b5b8;
    --ink: #2b2b2b;
    --muted: #6d6d6d;
    --field: #ececee;
    --field-line: #cfcfd2;
  }
  * { box-sizing: border-box; }
  html, body {
    margin: 0;
    width: 747px;
    height: 1200px;
    overflow: hidden;
    background: var(--page);
  }
  .board { position: relative; width: 747px; height: 1200px; }
  .variant { position: absolute; width: 335px; }
  .variant-label {
    margin: 0 0 8px;
    height: 12px;
    font: 400 11px/12px "Fira Mono", monospace;
    color: var(--ink);
  }
  .variant-art { display: block; width: 335px; height: 331px; }
  .col-a { left: 24px; } .col-b { left: 391px; }
  .row-1 { top: 14px; } .row-2 { top: 414px; } .row-3 { top: 814px; }

  svg text { font-family: "Comfortaa", sans-serif; }
  .stage { fill: var(--stage); }
  .phone { fill: var(--sheet); }
  .title { fill: #fff; font-size: 28px; }
  .card-label { fill: var(--ink); font-size: 12px; text-anchor: middle; }
  .link-text { font-size: 9px; text-anchor: middle; }
  .links-dark { fill: var(--ink); }
  .links-light { fill: #fff; }
  .back-text { fill: var(--muted); font-size: 11px; }
  .screen-title { fill: var(--ink); font-size: 21px; }
  .tag { fill: var(--gold); }
  .tag-text { fill: #fff; font-size: 13px; }
  .field { fill: var(--field); stroke: var(--field-line); stroke-width: 1; }
  .placeholder { fill: #a9a9ad; font-size: 9px; }
  .connect-text { fill: var(--ink); font-size: 9px; text-anchor: middle; }
  .brand-text { fill: var(--ink); font-size: 11px; font-weight: 600; }
  .brand-mark { fill: var(--gold); }
  .chevron { fill: none; stroke: #fff; stroke-width: 2; stroke-linecap: round; stroke-linejoin: round; }
  .chevron-dark { fill: none; stroke: var(--muted); stroke-width: 1.4; stroke-linecap: round; stroke-linejoin: round; }
  .cross { stroke: #fff; stroke-width: 1.3; stroke-linecap: round; }
  .fill-gold { fill: var(--gold); }
  .fill-gold-deep { fill: var(--gold-deep); }
  .fill-sun { fill: var(--sun); }
  .fill-slate { fill: var(--slate); }
  .fill-slate-deep { fill: var(--slate-deep); }
  .fill-mist { fill: var(--mist); }
  .edge-cream { fill: none; stroke: var(--cream); stroke-width: 7; stroke-linecap: round; }
  .pattern-spot { fill: #d9d6cc; }
</style>
</head>
<body>

<svg width="0" height="0" style="position:absolute" aria-hidden="true">
  <defs>
    <filter id="lift" x="-20%" y="-20%" width="140%" height="140%">
      <feDropShadow dx="0" dy="2" stdDeviation="3" flood-color="#000" flood-opacity="0.08"/>
    </filter>
    <clipPath id="clip-left"><rect x="50" y="55" width="247" height="546" rx="16"/></clipPath>
    <clipPath id="clip-right"><rect x="372" y="55" width="247" height="546" rx="16"/></clipPath>

    <radialGradient id="gold-fade" cx="0.15" cy="0.35" r="0.9">
      <stop offset="0" stop-color="#cbb271"/>
      <stop offset="1" stop-color="#f4efe2"/>
    </radialGradient>
    <linearGradient id="sun-fade" x1="0" y1="1" x2="0" y2="0">
      <stop offset="0" stop-color="#fdf1c8"/>
      <stop offset="1" stop-color="#fdc22e"/>
    </linearGradient>
    <linearGradient id="mist-fade" x1="0" y1="0" x2="1" y2="0">
      <stop offset="0" stop-color="#b3a98a"/>
      <stop offset="1" stop-color="#b4b5b8"/>
    </linearGradient>

    <g id="left-ui">
      <polyline class="chevron" points="70,74 64,80 70,86"/>
      <text class="title" x="70" y="152">Tell me</text>
      <text class="title" x="70" y="180">about you</text>
      <g filter="url(#lift)" fill="#fff">
        <rect x="70" y="212" width="98" height="68"/><rect x="180" y="212" width="98" height="68"/>
        <rect x="70" y="289" width="98" height="68"/><rect x="180" y="289" width="98" height="68"/>
        <rect x="70" y="366" width="98" height="68"/><rect x="180" y="366" width="98" height="68"/>
        <rect x="70" y="442" width="98" height="68"/><rect x="180" y="442" width="98" height="68"/>
      </g>
      <text class="card-label" x="119" y="244">Places</text><text class="card-label" x="119" y="257">I've Lived</text>
      <text class="card-label" x="229" y="244">Schools I've</text><text class="card-label" x="229" y="257">Attented</text>
      <text class="card-label" x="119" y="322">Where</text><text class="card-label" x="119" y="335">I worked</text>
      <text class="card-label" x="229" y="319">People</text><text class="card-label" x="229" y="332">I Know</text>
      <text class="card-label" x="119" y="398">Events I've</text><text class="card-label" x="119" y="411">Attended</text>
      <text class="card-label" x="229" y="398">Events I'm</text><text class="card-label" x="229" y="411">Attending</text>
      <text class="card-label" x="119" y="474">Music I</text><text class="card-label" x="119" y="487">Love</text>
      <text class="card-label" x="229" y="474">Teams</text><text class="card-label" x="229" y="487">I love</text>
    </g>

    <g id="text-links">
      <text class="link-text" x="120" y="574">Text Link 1</text>
      <text class="link-text" x="228" y="574">Text Link 2</text>
    </g>

    <g id="places-screen">
      <rect class="phone" x="372" y="135" width="247" height="480" rx="16"/>
      <polyline class="chevron-dark" points="400,159 396,164 400,169"/>
      <text class="back-text" x="407" y="168">back</text>
      <text class="screen-title" x="408" y="213">Places</text>
      <text class="screen-title" x="408" y="236">I've Lived</text>
      <rect class="tag" x="408" y="264" width="176" height="30"/>
      <text class="tag-text" x="419" y="284">Rome</text>
      <path class="cross" d="M570,275 l8,8 M578,275 l-8,8"/>
      <rect class="tag" x="408" y="297" width="176" height="30"/>
      <text class="tag-text" x="419" y="317">Bruxelles</text>
      <path class="cross" d="M570,308 l8,8 M578,308 l-8,8"/>
      <rect class="tag" x="408" y="331" width="176" height="30"/>
      <text class="tag-text" x="419" y="351">Madrid</text>
      <path class="cross" d="M570,342 l8,8 M578,342 l-8,8"/>
      <rect class="field" x="408.5" y="404.5" width="176" height="28"/>
      <text class="placeholder" x="420" y="422">Type a city</text>
      <text class="connect-text" x="496" y="463">or simply connect with</text>
      <rect class="brand-mark" x="418" y="509" width="9" height="9"/>
      <text class="brand-text" x="431" y="518">Fendora</text>
      <rect class="brand-mark" x="505" y="509" width="9" height="9"/>
      <text class="brand-text" x="518" y="518">WorkLoop</text>
    </g>

    <polyline id="right-chevron" class="chevron" points="392,74 386,80 392,86"/>
    <path id="corner-left" class="fill-slate" d="M50,55 H104 C104,82 88,104 50,110 Z"/>
    <path id="corner-right" class="fill-slate-deep" d="M372,55 H426 C426,82 410,104 372,110 Z"/>
  </defs>
</svg>

<main class="board">

  <section class="variant col-a row-1">
    <h2 class="variant-label">Gold 1</h2>
    <svg class="variant-art" viewBox="0 0 678 671">
      <rect class="stage" width="678" height="671"/>
      <rect class="phone" x="50" y="55" width="247" height="546" rx="16" filter="url(#lift)"/>
      <g clip-path="url(#clip-left)">
        <path class="fill-gold" d="M50,55 H297 V236 C294,292 246,302 204,330 C150,366 82,334 50,392 Z"/>
        <path class="fill-sun" d="M174,601 C180,542 220,522 258,510 C286,500 297,470 297,432 V601 Z"/>
        <use href="#corner-left"/>
      </g>
      <use href="#left-ui"/><use href="#text-links" class="links-dark"/>
      <rect class="phone" x="372" y="55" width="247" height="546" rx="16" filter="url(#lift)"/>
      <g clip-path="url(#clip-right)">
        <rect class="fill-gold-deep" x="372" y="55" width="247" height="110"/>
        <use href="#corner-right"/>
        <use href="#places-screen"/>
      </g>
      <use href="#right-chevron"/>
    </svg>
  </section>

  <section class="variant col-b row-1">
    <h2 class="variant-label">Gold 1b</h2>
    <svg class="variant-art" viewBox="0 0 678 671">
      <rect class="stage" width="678" height="671"/>
      <rect class="phone" x="50" y="55" width="247" height="546" rx="16" filter="url(#lift)"/>
      <g clip-path="url(#clip-left)">
        <path class="edge-cream" d="M297,240 C294,296 246,306 204,334 C150,370 82,338 50,396"/>
        <path class="fill-gold" d="M50,55 H297 V236 C294,292 246,302 204,330 C150,366 82,334 50,392 Z"/>
        <path class="fill-sun" d="M174,601 C180,542 220,522 258,510 C286,500 297,470 297,432 V601 Z"/>
        <use href="#corner-left"/>
      </g>
      <use href="#left-ui"/><use href="#text-links" class="links-dark"/>
      <rect class="phone" x="372" y="55" width="247" height="546" rx="16" filter="url(#lift)"/>
      <g clip-path="url(#clip-right)">
        <rect class="fill-gold-deep" x="372" y="55" width="247" height="110"/>
        <use href="#corner-right"/>
        <use href="#places-screen"/>
      </g>
      <use href="#right-chevron"/>
    </svg>
  </section>

  <section class="variant col-a row-2">
    <h2 class="variant-label">Gold 2</h2>
    <svg class="variant-art" viewBox="0 0 678 671">
      <rect class="stage" width="678" height="671"/>
      <rect class="phone" x="50" y="55" width="247" height="546" rx="16" filter="url(#lift)"/>
      <g clip-path="url(#clip-left)">
        <circle class="fill-gold" cx="147" cy="110" r="100"/>
        <circle class="fill-sun" cx="257" cy="585" r="100"/>
        <use href="#corner-left"/>
      </g>
      <use href="#left-ui"/><use href="#text-links" class="links-dark"/>
      <rect class="phone" x="372" y="55" width="247" height="546" rx="16" filter="url(#lift)"/>
      <g clip-path="url(#clip-right)">
        <rect class="fill-mist" x="372" y="55" width="247" height="110"/>
        <circle class="fill-gold-deep" cx="469" cy="110" r="100"/>
        <use href="#corner-right"/>
        <use href="#places-screen"/>
      </g>
      <use href="#right-chevron"/>
    </svg>
  </section>

  <section class="variant col-b row-2">
    <h2 class="variant-label">Gold 3</h2>
    <svg class="variant-art" viewBox="0 0 678 671">
      <rect class="stage" width="678" height="671"/>
      <rect class="phone" x="50" y="55" width="247" height="546" rx="16" filter="url(#lift)"/>
      <g clip-path="url(#clip-left)">
        <path class="fill-gold" d="M50,55 H202 C206,86 236,104 236,148 C236,196 196,212 150,206 C106,200 72,214 50,236 Z"/>
        <path class="fill-sun" d="M166,580 C164,556 210,552 240,538 C262,528 266,502 297,498 V586 C276,604 182,606 166,580 Z"/>
        <g role="img" aria-label="Scattered dot pattern">
          <rect class="pattern-spot" x="244" y="70" width="52" height="56" rx="8"/>
        </g>
        <use href="#corner-left"/>
      </g>
      <use href="#left-ui"/><use href="#text-links" class="links-dark"/>
      <rect class="phone" x="372" y="55" width="247" height="546" rx="16" filter="url(#lift)"/>
      <g clip-path="url(#clip-right)">
        <rect class="fill-mist" x="372" y="55" width="247" height="110"/>
        <path class="fill-gold-deep" d="M372,55 H518 C520,90 540,110 556,140 H372 Z"/>
        <g role="img" aria-label="Scattered dot pattern">
          <rect class="pattern-spot" x="566" y="70" width="52" height="56" rx="8"/>
        </g>
        <use href="#corner-right"/>
        <use href="#places-screen"/>
      </g>
      <use href="#right-chevron"/>
    </svg>
  </section>

  <section class="variant col-a row-3">
    <h2 class="variant-label">Gold 4</h2>
    <svg class="variant-art" viewBox="0 0 678 671">
      <rect class="stage" width="678" height="671"/>
      <rect class="phone" x="50" y="55" width="247" height="546" rx="16" filter="url(#lift)"/>
      <g clip-path="url(#clip-left)">
        <circle cx="147" cy="110" r="100" fill="url(#gold-fade)"/>
        <circle cx="257" cy="585" r="100" fill="url(#sun-fade)"/>
        <use href="#corner-left"/>
      </g>
      <use href="#left-ui"/><use href="#text-links" class="links-dark"/>
      <rect class="phone" x="372" y="55" width="247" height="546" rx="16" filter="url(#lift)"/>
      <g clip-path="url(#clip-right)">
        <rect x="372" y="55" width="247" height="110" fill="url(#mist-fade)"/>
        <use href="#corner-right"/>
        <use href="#places-screen"/>
      </g>
      <use href="#right-chevron"/>
    </svg>
  </section>

  <section class="variant col-b row-3">
    <h2 class="variant-label">Gold 5</h2>
    <svg class="variant-art" viewBox="0 0 678 671">
      <rect class="stage" width="678" height="671"/>
      <rect class="phone" x="50" y="55" width="247" height="546" rx="16" filter="url(#lift)"/>
      <g clip-path="url(#clip-left)">
        <path class="fill-gold" d="M50,55 H297 V296 L50,344 Z"/>
        <path class="fill-slate" d="M50,478 L297,420 V601 H50 Z"/>
        <use href="#corner-left"/>
      </g>
      <use href="#left-ui"/><use href="#text-links" class="links-light"/>
      <rect class="phone" x="372" y="55" width="247" height="546" rx="16" filter="url(#lift)"/>
      <g clip-path="url(#clip-right)">
        <rect class="fill-gold-deep" x="372" y="55" width="247" height="110"/>
        <use href="#corner-right"/>
        <use href="#places-screen"/>
      </g>
      <use href="#right-chevron"/>
    </svg>
  </section>

</main>
</body>
</html>
```